Creative and Fun Farm Metal Signage in the Barn

This will be featured in the farm. to make it more unique, the measurement will be 90cm x 60cm. This sign will be made by Metal and display inside the Barn. do have 2 A4 pockets available for them to slip in the cow's birth certificate. please make it fun and professional look. i have attached few photos that show rough idea of how we want it to be.

Target Market(s)

Restaurants or Hotels

Requirements
Must have
• Include 2 A4s certificate as stated, the logo and reserver for logo as well..
Nice to have
• This is a design of Signage where we will put it up in the barn.. this will consist a logo, Reserved by, and 2 A4 paper to slip in. be creative on the design

```html
<!DOCTYPE html>
<html lang="en">
<head>
<meta charset="utf-8">
<title>Kestrel Downs – Barn Signage</title>
<link href="https://fonts.googleapis.com/css2?family=Libre+Baskerville:wght@700&family=Stardos+Stencil:wght@700&display=swap" rel="stylesheet">
<style>
  :root{
    --page:#d0d1d3;
    --metal-light:#3c3c3c;
    --metal-dark:#121212;
    --cut:#d6d7d9;
    --panel:#ffffff;
    --ink:#2a2a2a;
    --paper:#ece8bf;
  }
  html,body{margin:0;padding:0;overflow:hidden;}
  body{width:960px;height:1200px;background:var(--page);position:relative;}
  .sign{position:absolute;left:117px;width:726px;height:484px;border-radius:33px;
    background:radial-gradient(ellipse at 55% 60%,var(--metal-light) 0%,#222 55%,var(--metal-dark) 100%);
    overflow:hidden;}
  .sign--filled{top:118px;}
  .sign--blank{top:635px;}
  .sign__shapes{position:absolute;inset:0;}
  .sign__heading{position:absolute;top:20px;left:0;right:0;text-align:center;margin:0;
    font-family:"Libre Baskerville",serif;font-weight:700;font-size:25px;letter-spacing:2px;color:var(--cut);}
  .sign__brand{position:absolute;top:118px;left:30px;width:520px;text-align:center;margin:0;
    font-family:"Libre Baskerville",serif;font-weight:700;font-size:58px;color:var(--cut);}
  .reserved__label{position:absolute;left:25px;width:286px;top:296px;text-align:center;
    font-family:"Stardos Stencil",sans-serif;font-weight:700;font-size:24px;letter-spacing:2px;color:var(--cut);line-height:1;}
  .reserved__panel{position:absolute;left:44px;top:332px;width:247px;height:103px;border-radius:12px;
    background:var(--panel);display:flex;align-items:center;justify-content:center;}
  .reserved__name{font-family:"Libre Baskerville",serif;font-weight:700;font-size:19px;color:var(--ink);letter-spacing:1px;}
  .certificates{position:absolute;left:460px;top:225px;width:243px;height:234px;
    background:linear-gradient(160deg,#f2efcc,var(--paper));box-shadow:0 2px 6px rgba(0,0,0,.6);}
</style>
</head>
<body>
<svg width="0" height="0" style="position:absolute">
  <defs>
    <symbol id="star" viewBox="-1 -1 2 2">
      <polygon points="0,-1 0.195,-0.405 0.782,-0.623 0.439,-0.1 0.975,0.223 0.352,0.28 0.434,0.901 0,0.45 -0.434,0.901 -0.352,0.28 -0.975,0.223 -0.439,-0.1 -0.782,-0.623 -0.195,-0.405" fill="#d6d7d9"/>
    </symbol>
  </defs>
</svg>

<section class="sign sign--filled">
  <svg class="sign__shapes" viewBox="0 0 726 484" aria-hidden="true">
    <use href="#star" x="590" y="99" width="80" height="80"/>
    <use href="#star" x="44" y="226" width="28" height="28"/>
    <use href="#star" x="234" y="241" width="28" height="28"/>
    <use href="#star" x="535" y="196" width="22" height="22"/>
    <use href="#star" x="419" y="285" width="28" height="28"/>
    <use href="#star" x="362" y="407" width="28" height="28"/>
    <g fill="none" stroke="#d6d7d9" stroke-width="7">
      <path d="M25 345 V320 Q25 298 47 298 H60"/>
      <path d="M276 298 H289 Q311 298 311 320 V345"/>
      <path d="M25 365 V435 Q25 457 47 457 H160"/>
      <path d="M176 457 H289 Q311 457 311 435 V365"/>
    </g>
  </svg>
  <h1 class="sign__heading">• AUSTRALIAN PREMIUM WAGYU BEEF •</h1>
  <p class="sign__brand">Kestrel Downs</p>
  <div class="reserved__label">RESERVED FOR</div>
  <div class="reserved__panel"><span class="reserved__name">HARBOURVIEW HOTELS</span></div>
  <div class="certificates" role="img" aria-label="Two A4 pockets holding cattle birth certificates, with decorative scroll overlay"></div>
</section>

<section class="sign sign--blank">
  <svg class="sign__shapes" viewBox="0 0 726 484" aria-hidden="true">
    <use href="#star" x="590" y="99" width="80" height="80"/>
    <use href="#star" x="44" y="226" width="28" height="28"/>
    <use href="#star" x="234" y="241" width="28" height="28"/>
    <use href="#star" x="535" y="196" width="22" height="22"/>
    <use href="#star" x="419" y="285" width="28" height="28"/>
    <use href="#star" x="362" y="407" width="28" height="28"/>
    <g fill="none" stroke="#d6d7d9" stroke-width="7">
      <path d="M25 345 V320 Q25 298 47 298 H60"/>
      <path d="M276 298 H289 Q311 298 311 320 V345"/>
      <path d="M25 365 V435 Q25 457 47 457 H160"/>
      <path d="M176 457 H289 Q311 457 311 435 V365"/>
      <rect x="44" y="332" width="247" height="103" rx="14" stroke-width="5"/>
    </g>
    <g fill="none" stroke="#d6d7d9" stroke-width="13">
      <path d="M468 458 A300 300 0 0 1 703 222"/>
      <path d="M508 458 A260 260 0 0 1 703 262"/>
    </g>
    <path d="M548 458 A220 220 0 0 1 703 302 V458 Z" fill="#c9cacc" role="img" aria-label="Decorative scroll ornament in corner"/>
  </svg>
  <h2 class="sign__heading">• AUSTRALIAN PREMIUM WAGYU BEEF •</h2>
  <p class="sign__brand">Kestrel Downs</p>
  <div class="reserved__label">RESERVED FOR</div>
</section>
</body>
</html>
```